Teskar Business Cards

We need new Business Cards for our startup. It just launched.It is working in the high-end it-market. Specifically in the cloud area. We are a hybrid cloud company. The company logo is attached. We are a Swiss based company. Information visible on the card is: 1. Logo 2. Company Name: Teskar AG 3. Subtitle: Hybrid Clouds. 3. Name: Lukas Brenner 4. Adress: Holderweg 12a, 8462 Mattenried, Elvaria 5. Email: lukas@teskar.example. 6. Mobile: +41 79 304 62 18. It should be a grey/white design. Similar to the attached logo. It should have class, high-quality but not too much color and no gold used.

I forgot to add my Position. Please use Founder / CEO. thanks lukas

```html
<!DOCTYPE html>
<html lang="en">
<head>
<meta charset="utf-8">
<title>Teskar AG – Business Card</title>
<link rel="stylesheet" href="https://fonts.googleapis.com/css2?family=Lato:wght@300;400;700&display=swap">
<style>
  :root {
    --backdrop: #6f6f6f;
    --card-white: #ffffff;
    --band-grey: #c9c9c9;
    --card-dark: #1f1f1f;
    --ink-dark: #1c1c1c;
    --ink-logo: #4a4a4a;
    --ink-name: #8c8c8c;
    --ink-role: #a3a3a3;
    --ink-contact: #7a7a7a;
    --ink-label: #9a9a9a;
  }
  * { margin: 0; padding: 0; box-sizing: border-box; }
  html, body {
    width: 1200px;
    height: 900px;
    overflow: hidden;
    background: var(--backdrop);
    font-family: "Lato", sans-serif;
  }
  .canvas {
    width: 1200px;
    height: 900px;
    display: flex;
    align-items: center;
    justify-content: center;
  }
  .card {
    width: 1000px;
    height: 660px;
    border-radius: 34px;
    overflow: hidden;
    display: flex;
    flex-direction: column;
    background: var(--card-dark);
  }
  .card__brand {
    height: 270px;
    background: var(--card-white);
    display: flex;
    align-items: center;
    justify-content: center;
    gap: 36px;
  }
  .brand-mark {
    width: 64px;
    height: 64px;
    border-radius: 50%;
    background: var(--ink-logo);
  }
  .brand-name {
    font-weight: 300;
    font-size: 58px;
    letter-spacing: 0.32em;
    color: var(--ink-logo);
  }
  .card__band {
    height: 80px;
    background: var(--band-grey);
    display: flex;
    align-items: center;
    justify-content: center;
    color: var(--ink-dark);
    font-size: 32px;
  }
  .band__company { font-weight: 700; }
  .band__tagline { font-weight: 400; font-size: 26px; margin-left: 10px; }
  .card__person {
    flex: 1;
    display: flex;
    flex-direction: column;
    align-items: center;
    justify-content: center;
    text-align: center;
    padding-bottom: 16px;
  }
  .person__name {
    font-size: 52px;
    font-weight: 400;
    color: var(--ink-name);
    letter-spacing: 0.01em;
    line-height: 1.1;
  }
  .person__name strong { font-weight: 700; }
  .person__role {
    margin-top: 8px;
    font-size: 24px;
    color: var(--ink-role);
    letter-spacing: 0.04em;
  }
  .person__contact {
    margin-top: 26px;
    font-size: 27px;
    color: var(--ink-contact);
    display: flex;
    gap: 48px;
  }
  .contact__label { font-weight: 700; color: var(--ink-label); margin-right: 6px; }
  .person__address {
    margin-top: 8px;
    font-size: 31px;
    color: var(--ink-contact);
  }
</style>
</head>
<body>
  <main class="canvas">
    <article class="card">
      <header class="card__brand">
        <span class="brand-mark" aria-hidden="true"></span>
        <span class="brand-name">TESKAR</span>
      </header>
      <div class="card__band">
        <span class="band__company">TESKAR AG</span>
        <span class="band__tagline">- HYBRID CLOUDS</span>
      </div>
      <section class="card__person">
        <h1 class="person__name"><strong>LUKAS</strong> BRENNER</h1>
        <p class="person__role">FOUNDER / CEO</p>
        <p class="person__contact">
          <span><span class="contact__label">e.</span>lukas@teskar.example</span>
          <span><span class="contact__label">m.</span>+41 79 304 62 18</span>
        </p>
        <p class="person__address">Holderweg 12a, 8462 Mattenried, Elvaria</p>
      </section>
    </article>
  </main>
</body>
</html>
```